tarnwell crest works ltd commercial solar installs

a bifold A4 brochure , explaining the benefits of solar panel and battery storage on commercial buildings in England

i dont have many images or paragraphs i was hoping that this could be part of your design

```html
<!DOCTYPE html>
<html lang="en">
<head>
<meta charset="utf-8">
<title>Tarnwell Crest Works Ltd – Commercial Solar Installs Brochure</title>
<link href="https://fonts.googleapis.com/css2?family=Arimo:wght@400;700&display=swap" rel="stylesheet">
<style>
:root{
  --navy:#1f2b52;
  --green:#2fb52f;
  --green-dark:#0c5c12;
  --lime:#b8f200;
  --tag:#3ccc2b;
  --text:#2b2b2b;
  --page-bg:#e4e4e4;
}
*{box-sizing:border-box;margin:0;padding:0}
html,body{width:1200px;height:2738px;overflow:hidden}
body{background:var(--page-bg);font-family:"Arimo",Arial,sans-serif;position:relative}

.spread{position:absolute;left:93px;width:1014px;height:781px;background:#fff;overflow:hidden;box-shadow:0 2px 8px rgba(0,0,0,.18)}
.spread--cover{top:578px}
.spread--inside{top:1379px}
.spread-art{position:absolute;inset:0;width:1014px;height:781px;display:block}

/* cover */
.cover-title{position:absolute;left:560px;top:62px;width:400px;text-align:center;color:var(--navy);font-weight:700;font-size:45px;line-height:48px;letter-spacing:.5px}
.cover-company{position:absolute;left:119px;top:565px;color:#fff;font-size:22px;letter-spacing:.6px}
.cover-rule{position:absolute;left:30px;top:615px;width:452px;height:2px;background:var(--green)}
.cover-cta{position:absolute;left:96px;top:628px;color:var(--lime);font-weight:700;font-size:19px;line-height:22px;text-align:center;width:180px}
.phone-block{position:absolute;left:39px;top:674px;display:flex;height:44px}
.phone-block__icon{width:44px;height:44px;background:var(--green-dark);border-radius:4px;display:flex;align-items:center;justify-content:center}
.phone-block__number{margin-left:4px;background:var(--lime);border-radius:3px;padding:0 10px;font-weight:700;font-size:27px;line-height:44px;color:#111;width:196px}
.cover-divider{position:absolute;left:316px;top:636px;width:1px;height:56px;background:rgba(255,255,255,.7)}
.cover-address{position:absolute;left:331px;top:630px;color:#fff;font-size:11.5px;line-height:13px}
.cover-address__row{display:flex;gap:6px;align-items:flex-start}
.cover-address__row + .cover-address__row{margin-top:4px}
.accreditations{position:absolute;left:140px;top:728px;width:226px;height:53px;background:#fff;display:flex;align-items:center;justify-content:space-around;padding:0 10px}
.accreditations__badge{height:18px;background:#d9d9d9}
.accreditations__badge--a{width:62px;border-radius:3px;background:#e7b3b3}
.accreditations__badge--b{width:40px;border-radius:3px;background:#b9cde6}
.accreditations__badge--c{width:48px;height:34px;border-radius:3px;background:#c9a6d6}
.back-cta{position:absolute;left:636px;top:706px;color:#fff;font-weight:700;font-size:11.5px;width:240px;text-align:center}
.back-phone{position:absolute;left:686px;top:728px;height:26px;width:152px;background:var(--green);border-radius:13px;display:flex;align-items:center;gap:6px;padding-left:6px;color:var(--lime);font-weight:700;font-size:16px}
.back-phone__icon{width:20px;height:20px;border-radius:50%;background:var(--green-dark);display:flex;align-items:center;justify-content:center}

/* inside */
.inside-heading{position:absolute;left:36px;top:28px;color:var(--lime);font-weight:700;font-size:27px;line-height:32px;letter-spacing:.3px}
.column{position:absolute;width:447px;color:var(--text);font-size:9.2px;line-height:11.2px;text-align:justify}
.column p + p{margin-top:9px}
.section{position:absolute;width:447px}
.section-tag{display:inline-block;background:var(--tag);color:var(--green-dark);font-weight:700;font-size:18px;line-height:22px;padding:0 6px;border-radius:3px;margin-bottom:8px;border:1px solid #7fe06f}
.section p{color:var(--text);font-size:9.2px;line-height:11.2px;text-align:justify}
.section p + p{margin-top:9px}
.narrow{margin-right:118px}
.section--planet{left:34px;top:160px}
.section--money{left:34px;top:398px}
.section--charging{left:34px;top:650px}
.column--right{left:538px;top:181px}
.section--storage{left:538px;top:318px}
.art-slot{position:absolute;display:block;border-radius:4px}
.art-slot--planet{left:376px;top:277px;width:128px;height:110px;background:radial-gradient(circle,#cfe8b4 0,#a6d27c 60%,#e8f3dc 100%)}
.art-slot--money{left:368px;top:508px;width:122px;height:86px;background:linear-gradient(135deg,#f0dcc0,#e8b98f 55%,#cfc6b5)}
.art-slot--house{left:560px;top:0;width:454px;height:168px;background:linear-gradient(180deg,#ffffff 0,#e5eefb 55%,#cfdcf2 100%);border-radius:0}
.art-slot--battery{left:762px;top:625px;width:240px;height:150px;background:linear-gradient(160deg,#3a6fd8,#7ad23a 70%,#2f8f2a);border-radius:0}
</style>
</head>
<body>

<section class="spread spread--cover" aria-label="Brochure cover spread">
  <svg class="spread-art" viewBox="0 0 1014 781" xmlns="http://www.w3.org/2000/svg">
    <defs>
      <linearGradient id="sceneFill" x1="0" y1="0" x2="0" y2="1">
        <stop offset="0" stop-color="#f4ecd4"/>
        <stop offset="0.7" stop-color="#e6e9ee"/>
        <stop offset="1" stop-color="#8e9198"/>
      </linearGradient>
      <linearGradient id="photoFill" x1="0" y1="0" x2="1" y2="1">
        <stop offset="0" stop-color="#5e6f93"/>
        <stop offset="0.45" stop-color="#7b8397"/>
        <stop offset="0.75" stop-color="#6f7a5a"/>
        <stop offset="1" stop-color="#4d6b34"/>
      </linearGradient>
      <linearGradient id="swoosh" x1="0" y1="1" x2="1" y2="0">
        <stop offset="0" stop-color="#1f9e1f"/>
        <stop offset="1" stop-color="#7fdc1c"/>
      </linearGradient>
    </defs>
    <rect width="1014" height="781" fill="#fff"/>
    <rect x="0" y="0" width="585" height="420" fill="url(#sceneFill)" role="img" aria-label="Illustration of a commercial building with rooftop solar panels and an electric car charging outside"/>
    <path d="M0,452 C300,330 620,215 1014,190 L1014,781 L0,781 Z" fill="url(#photoFill)" role="img" aria-label="Photo of a solar technician holding an orange hard hat and drill beside a ground-mounted solar panel array"/>
    <path d="M0,602 L490,602 L490,781 L0,781 Z" fill="#55516a" opacity="0.86"/>
    <path d="M0,420 C300,298 620,190 1014,170 L1014,192 C620,218 300,332 0,455 Z" fill="url(#swoosh)"/>
    <path d="M0,458 C300,336 620,222 1014,196 L1014,200 C620,226 300,342 0,464 Z" fill="#c6f53a"/>
  </svg>

  <h1 class="cover-title">COMMERCIAL SOLAR INSTALLS</h1>

  <p class="cover-company">Tarnwell Crest Works Ltd</p>
  <div class="cover-rule"></div>
  <p class="cover-cta">Talk To Us Today<br>Book A Home Visit</p>

  <div class="phone-block">
    <div class="phone-block__icon">
      <svg width="24" height="24" viewBox="0 0 24 24" aria-hidden="true"><path d="M6.6 10.8c1.4 2.8 3.8 5.1 6.6 6.6l2.2-2.2c.3-.3.7-.4 1-.2 1.1.4 2.3.6 3.6.6.6 0 1 .4 1 1V20c0 .6-.4 1-1 1C10.6 21 3 13.4 3 4c0-.6.4-1 1-1h3.5c.6 0 1 .4 1 1 0 1.3.2 2.5.6 3.6.1.3 0 .7-.2 1z" fill="#b8f200"/></svg>
    </div>
    <div class="phone-block__number">01632 960418</div>
  </div>

  <div class="cover-divider"></div>
  <div class="cover-address">
    <div class="cover-address__row">
      <svg width="9" height="12" viewBox="0 0 9 12" aria-hidden="true"><path d="M4.5 0C2 0 0 2 0 4.5 0 8 4.5 12 4.5 12S9 8 9 4.5C9 2 7 0 4.5 0zm0 6.2a1.7 1.7 0 110-3.4 1.7 1.7 0 010 3.4z" fill="#b8f200"/></svg>
      <span>7 Harrow Court Business Park<br>Fenley<br>Kent ME99 4QT</span>
    </div>
    <div class="cover-address__row">
      <svg width="11" height="11" viewBox="0 0 12 12" aria-hidden="true"><circle cx="6" cy="6" r="5" fill="none" stroke="#b8f200" stroke-width="1.2"/><path d="M1 6h10M6 1c2 2 2 8 0 10M6 1c-2 2-2 8 0 10" fill="none" stroke="#b8f200" stroke-width="1"/></svg>
      <span>www.tarnwellcrest.co</span>
    </div>
  </div>

  <div class="accreditations" aria-label="Trade accreditations">
    <span class="accreditations__badge accreditations__badge--a"></span>
    <span class="accreditations__badge accreditations__badge--b"></span>
    <span class="accreditations__badge accreditations__badge--c"></span>
  </div>

  <p class="back-cta">TALK TO US TODAY BOOK A HOME VISIT</p>
  <div class="back-phone">
    <span class="back-phone__icon"><svg width="12" height="12" viewBox="0 0 24 24" aria-hidden="true"><path d="M6.6 10.8c1.4 2.8 3.8 5.1 6.6 6.6l2.2-2.2c.3-.3.7-.4 1-.2 1.1.4 2.3.6 3.6.6.6 0 1 .4 1 1V20c0 .6-.4 1-1 1C10.6 21 3 13.4 3 4c0-.6.4-1 1-1h3.5c.6 0 1 .4 1 1 0 1.3.2 2.5.6 3.6.1.3 0 .7-.2 1z" fill="#b8f200"/></svg></span>
    01632 960418
  </div>
</section>

<section class="spread spread--inside" aria-label="Brochure inside spread">
  <div class="art-slot art-slot--house" role="img" aria-label="Illustration of a modern house with an electric car charging in the garage and a family walking nearby"></div>
  <svg class="spread-art" viewBox="0 0 1014 781" xmlns="http://www.w3.org/2000/svg" aria-hidden="true">
    <path d="M0,0 L760,0 C560,70 300,125 0,130 Z" fill="#1f2b52"/>
    <path d="M0,130 C300,125 560,70 760,0 L800,0 C600,95 330,160 0,172 Z" fill="#2fb52f"/>
    <path d="M0,172 C330,160 600,95 800,0 L812,0 C610,104 340,168 0,180 Z" fill="#b8f200"/>
    <path d="M390,781 C620,760 830,700 1014,615 L1014,781 Z" fill="#2fb52f"/>
    <path d="M470,781 C680,766 860,720 1014,650 L1014,781 Z" fill="#1d5fc2"/>
  </svg>

  <h2 class="inside-heading">Why start using<br>TARNWELL CREST WORKS TODAY?</h2>

  <div class="art-slot art-slot--planet" role="img" aria-label="Illustration of hands holding a globe with the words save the planet"></div>
  <div class="art-slot art-slot--money" role="img" aria-label="Illustration of a hand holding banknotes and a pound coin"></div>
  <div class="art-slot art-slot--battery" role="img" aria-label="Illustration of a house made of solar panels over a row of green batteries"></div>

  <div class="section section--planet">
    <span class="section-tag">Save the planet?</span>
    <p>Climate change is real and it's happening today. Our world will change irreparably if we do not change our way of living today. By reducing your own CO2 emissions and installing solar-powered energy systems then you are doing your bit to help save our planet from a climate disaster.</p>
    <p>The directors and employees at Tarnwell Crest Works, have been installing solar power systems for over 15 years all across the southeast of England and have the experience necessary to complete even the most complex of installations.</p>
    <p class="narrow">In truth, solar power can now be installed in under a day for most homes and is very affordable. Solar energy is the planet's most abundant, energy source available.</p>
    <p class="narrow">There are two ways that solar technologies harness solar energy, Solar Photovoltaics and Solar Thermal. Solar Photovoltaic (or PV) is a technology that converts our sunlight into direct current electricity by using semiconductors. Alternatively, Solar Thermal is a technology which uses the heat and energy from the sun for heating or producing electricity.</p>
  </div>

  <div class="section section--money">
    <span class="section-tag">Save you money?</span>
    <p>Using solar power to produce your heating and electricity supply at home can fully repay your initial investment over time.</p>
    <p>Under the smart export guarantee (SEG) scheme which was launched in January 2020, households get paid for solar energy they 'export'. This is electricity you generate, but don't use yourself, which is then pumped back into the national energy grid.</p>
    <p class="narrow">With electric prices at a record high and the predictions that they will continue to rise over the next few years, it's never been a better time to invest in solar power. Solar panels can last over 40 years so upgrading your energy delivery system today can enable you to lock into a much cheaper way to heat and power your home and avoid any large price hikes for the foreseeable future.</p>
    <p class="narrow">Our solar energy, friendly team is on hand to help with your questions today, so feel free to get in touch on 01632 960418.</p>
    <p>Solar power can save you money today and even more in the future.</p>
  </div>

  <div class="section section--charging">
    <span class="section-tag">Home Car Charging</span>
    <p>Tarnwell Crest Works can install most electric car charging points at your home in just one day.</p>
    <p>Typically plug-in hybrids such as a Lumen charge at a rate of 3.7kW, and reach maximum charge in under 3 hours however fully electric cars such as a Corvane can charge at 7.4kW on a single-phase supply but have a much bigger battery. Typically it will take you up to 10 hours to charge a fully electric car. A 3.7kW charges at a rate of approximately 12mph, a 7.4kW will charge at a rate of approximately 24mph.</p>
    <p>Can my solar panels charge my electric car?</p>
  </div>

  <div class="column column--right">
    <p>Yes, there are a couple of ways to do this. One is to use the Solvane charger or an equivalent that diverts excess power generation into an electric vehicle. This way, what would have been exported back to the grid is now providing you with zero-carbon footprint transport. Your electric car though must be parked at home during the daylight hours.</p>
    <p>The other alternative is to use a battery system to store this excess energy, and then discharge this into your EV in the evening. The battery would also cover your household electric requirements once the sunlight has disappeared for the day.</p>
    <p>As electric vehicles charge from an AC supply you cannot charge directly from solar so you will need an inverter to do this.</p>
  </div>

  <div class="section section--storage">
    <span class="section-tag">Home Energy Storage</span>
    <p>Home battery storage is an innovative way for energy-conscious consumers to help the planet out with some extra energy. If you have solar panels installed on your house roof, there's a pretty clear benefit to storing any unused or unwanted electricity in a battery to use at night or days when the sun is not shining so brightly.</p>
    <p>Home battery storage for unused electricity isn't new though. Off-grid solar or photovoltaic (PV) and wind electricity generation on properties not connected to a power source have used battery storage to capture the unused electricity for many years, however, now that new technology is available, this energy can be stored quicker and cheaper than ever before.</p>
    <p>Storage batteries are increasingly popular with new solar installations, along with adding an EV car charging point. Tarnwell Crest Works can provide you with a free quotation that includes all three installations, often all on the same day.</p>
    <p>If it's the money-saving aspect that appeals to you most or the fact that you are helping the planet to generate more energy from renewable sources or you just want to be off the grid, or all of the above, then installing solar panels, battery storage and EV car charging points in your home is definitely worth looking at.</p>
    <p>If your solar panel array and battery are large enough, you can run your home substantially on solar power. Using electricity from your battery can be cheaper per kilowatt-hour than using electricity from the grid, depending on the time of day and electricity tariffs in your area. Get in touch with Tarnwell Crest Works to find out more and start making those savings today.</p>
  </div>
</section>

</body>
</html>
```